依頼詳細
記載項目の内容を含んだ、 85.6mm × 54.0mmのICカード(一般的なカードと同じサイズ)に印刷可能なデザインをお願い致します。
カードは横向きなので、縦向きのデザインは不可と致します。

(1)弊社のロゴ(※添付ファイル)に合うもの
(2)「ハイテクさ(技術力)」「クリーンさ(清潔感)」
が感じられるデザインを求めております。

※ロゴの配色は、添付ファイルのもの(グラデーション)からデザインに合わせて変更し単色等にして頂いても問題ありません

・トンボ(トリムマーク)をつけて下さい。
・フチなしのデザインなどは必ず仕上がり線より外側に3mm程度の塗り足しを入れて下さい。
・顔写真または半身写真など:仮として、グレーに塗りつぶした人物のシルエットでデザインに入れ込んでください。
記載項目
●表面内容
①名前欄
②社員番号欄
③発行日欄
④顔写真欄
⑤会社名:KVT株式会社
⑥本社住所
〒241-0815
東雲県青葉市緑丘区北見坂3丁目8番21号
TEL 042-618-3940(代表) FAX 042-619-2856
⑦「上記のものは当社の従業員であることを証明する」の一文

●裏面内容
・弊社の経営理念
「時代と共に進化を続け、最適な快適環境を提供する」

・注意事項
本証は当社社員であることを証明するものである
このカードを他人に貸与又は譲渡しないこと
本証は常時携帯すること
本証を紛失、破損した場合は直ちに届け出ること
退職時は直ちに返納すること
本証を取得された方は当社にご連絡ください
希望イメージ
シンプル 複雑
単色 カラフル
暗い 明るい
日常 高級
遊び心 厳粛
未来的 伝統的
女性的 男性的
希望する色
青系、緑系、グレー系
納品ファイル
• 高解像度JPG (.jpg)
• イラストレーター形式 (.ai)
• フォトショップ形式 (.psd)
• PNG形式 (.png)
補足説明
他社の知的財産権・商標を侵すようなデザイン等の提案は決してしないようにお願い致します。
著作権の盗用や侵害するデザイン案は厳禁になります。
素材テンプレートの流用やアレンジも不可です。
皆様からのご提案、誠にありがとうございます。
よりイメージの付きやすいデザインが可能となるよう、希望内容を追記させていただく事となりました。
ご一読の程、よろしくお願い致します。

●追加希望内容
カラーはグラデーション等の効果よりも、シンプルなものがベストです
依頼内容を明確にするため、さらに追加したい点がございましたので、期間延長の上追記させて頂きます。ご確認の程よろしくお願い致します。

●写真のサイズは免許証と同じ程度の大きさでお願い致します
●写真素材を使用したものよりも、デザインのみのシンプルなものがベストです

表面・裏面共にシンプルかつスマートなデザインで、弊社内でも最も多数から好評でありましたので当選とさせて頂きました。

今回のコンペにご参加頂きました皆様、素晴らしいデザイン案を多数頂きまして誠にありがとうございます。

次回募集を行う事がございましたら、改めましてご参加頂ければ幸いです。

```html
<!DOCTYPE html>
<html lang="ja">
<head>
<meta charset="utf-8">
<title>KVT株式会社 社員証</title>
<link rel="stylesheet" href="https://fonts.googleapis.com/css2?family=Noto+Sans+JP:wght@400;500;700&family=Noto+Serif+JP:wght@700;900&family=Share+Tech+Mono&display=swap">
<style>
  :root {
    --page: #ffffff;
    --metal-light: #eef0f3;
    --metal-mid: #c9ced4;
    --metal-dark: #a9afb7;
    --navy: #1c2b4d;
    --ink: #2a3346;
    --brand: #1f5fae;
    --label-bg: #2b2f38;
    --photo-top: #d4d7db;
    --photo-bottom: #9ba1a8;
    --note-bg: rgba(255,255,255,0.78);
  }
  * { margin: 0; padding: 0; box-sizing: border-box; }
  html, body { width: 828px; height: 1200px; overflow: hidden; background: var(--page); }
  body { position: relative; font-family: "Noto Sans JP", sans-serif; color: var(--ink); }

  .card {
    position: absolute; left: 28px; width: 772px; height: 530px;
    border-radius: 22px; overflow: hidden;
    background:
      repeating-linear-gradient(0deg, rgba(255,255,255,0.14) 0 1px, rgba(0,0,0,0.03) 1px 3px),
      linear-gradient(160deg, var(--metal-light) 0%, var(--metal-mid) 45%, var(--metal-dark) 70%, var(--metal-light) 100%);
    box-shadow: 0 0 0 1px #b5bac1;
  }
  .card--front { top: 22px; }
  .card--back { top: 636px; }

  .punch-hole {
    position: absolute; left: 370px; top: 30px; width: 34px; height: 34px;
    border-radius: 50%; background: var(--page); box-shadow: inset 0 1px 3px rgba(0,0,0,0.25);
  }

  .badge-title { position: absolute; left: 24px; top: 30px; display: flex; gap: 4px; }
  .badge-title span {
    width: 40px; height: 40px; background: var(--label-bg); color: #fff;
    font-weight: 700; font-size: 27px; line-height: 40px; text-align: center;
  }

  .field { position: absolute; left: 26px; color: var(--ink); white-space: nowrap; }
  .field--name { top: 104px; font-size: 36px; font-weight: 500; letter-spacing: 2px; line-height: 1.2; }
  .field--name .label { font-family: "Share Tech Mono", monospace; font-size: 24px; margin-right: 12px; }
  .field--romaji { top: 152px; left: 142px; font-size: 15px; letter-spacing: 2px; }
  .field--id, .field--date { font-family: "Share Tech Mono", monospace; font-size: 30px; letter-spacing: 1px; line-height: 1.2; }
  .field--id { top: 186px; }
  .field--date { top: 246px; }
  .rule { position: absolute; left: 26px; height: 2px; background: var(--ink); opacity: 0.8; }
  .rule--id { top: 228px; width: 290px; }
  .rule--date { top: 288px; width: 190px; }
  .field--certify { top: 300px; font-size: 16px; }

  .brand { position: absolute; display: flex; align-items: center; gap: 12px; color: var(--brand); font-weight: 700; white-space: nowrap; }
  .brand__dot { border-radius: 50%; background: var(--brand); }
  .brand--front { left: 40px; top: 372px; font-size: 48px; }
  .brand--front .brand__dot { width: 44px; height: 44px; }

  .photo { position: absolute; left: 500px; top: 30px; width: 246px; height: 296px; background: linear-gradient(180deg, var(--photo-top), var(--photo-bottom)); border: 2px solid #fff; }

  .issuer { position: absolute; left: 460px; top: 356px; font-size: 14px; line-height: 1.65; color: var(--ink); white-space: nowrap; }
  .issuer .company { font-size: 16px; font-weight: 500; }

  .brand--back { left: 0; right: 0; top: 38px; justify-content: center; font-size: 50px; }
  .brand--back .brand__dot { width: 44px; height: 44px; }

  .philosophy {
    position: absolute; left: 0; right: 0; top: 122px; text-align: center;
    font-family: "Noto Serif JP", serif; font-weight: 900; font-size: 44px; line-height: 1.45; color: var(--navy);
  }

  .notes {
    position: absolute; left: 60px; top: 330px; width: 652px; height: 160px;
    border-radius: 18px; background: var(--note-bg); display: flex; align-items: center;
  }
  .notes__title { width: 200px; text-align: center; font-size: 20px; font-weight: 500; }
  .notes__list { list-style: none; font-size: 15px; line-height: 1.5; }
</style>
</head>
<body>
  <section class="card card--front" aria-label="社員証 表面">
    <div class="punch-hole"></div>
    <div class="badge-title"><span>社</span><span>員</span><span>証</span></div>

    <div class="field field--name"><span class="label">NAME</span>佐藤 健一</div>
    <div class="field field--romaji">KENICHI SATO</div>
    <div class="field field--id">ID:KVT0123456789</div>
    <div class="rule rule--id"></div>
    <div class="field field--date">DATE /2019-00-00</div>
    <div class="rule rule--date"></div>
    <div class="field field--certify">上記のものは当社の従業員であることを証明する</div>

    <div class="brand brand--front"><span class="brand__dot"></span>KVT Inc.</div>

    <div class="photo" role="img" aria-label="顔写真欄(グレーの人物シルエット)"></div>

    <div class="issuer">
      <div class="company">発行：KVT株式会社</div>
      <div>〒241-0815</div>
      <div>東雲県青葉市緑丘区北見坂3丁目8番21号</div>
      <div>TEL.042-618-3940(代表) FAX.042-619-2856</div>
    </div>
  </section>

  <section class="card card--back" aria-label="社員証 裏面">
    <div class="brand brand--back"><span class="brand__dot"></span>KVT株式会社</div>
    <p class="philosophy">時代と共に進化を続け、<br>最適な快適環境を提供する</p>
    <div class="notes">
      <div class="notes__title">【注意事項】</div>
      <ul class="notes__list">
        <li>本証は当社社員であることを証明するものである。</li>
        <li>このカードを他人に貸与又は譲渡しないこと。</li>
        <li>本証は常時携帯すること。</li>
        <li>本証を紛失、破損した場合は直ちに届け出ること。</li>
        <li>退職時は直ちに返納すること。</li>
        <li>※本証を取得された方は当社にご連絡ください。</li>
      </ul>
    </div>
  </section>
</body>
</html>
```